Bright Leaf Bistro & Pantry Squarespace Website Files

We need a Squarespace website for a new company called "Bright Leaf Bistro & Pantry".

The company is committed to providing the highest quality, fresh and natural food, health and wellness products.

We would like to see designs that use the colors of our logo. Please provide graphic design and layout for the site.

The final design should communicate health and wellness.

Target Market(s)

Bright Leaf Bistro & Pantry is a new company that will offer customers organic and
locally grown produce, chemical and preservative-free groceries, cruelty-free body care and eco-household products. Additionally, our kitchen will offer healthy lunch and dinner options emphasizing organic and whole food options, recognizing the trend within the restaurant industry for the demand for healthy cuisine. The restaurant will procure local foods when possible, reducing dependence on fossil fuels used for transportation. All of our products are healthy alternatives to the products available at conventional grocery chains.

Located in the heart of the growing Harlow Street section of Lewiston, NY, the
marketplace will serve a community of residents in Lewiston, residents in
Niagara Falls, and residents in Niagara Falls, Ontario, Canada.

The creation of the marketplace is in response to the growing demand in the community for a local natural food store.

Industry/Entity Type

Cafe

Font styles to use
Sans Serif

Colors
00a990
faa54b
87cfc7
f37122

Requirements
Must have
• Home page, Events, Cafe Menu, Marketplace Products, Health Info, News, Recipes, Contact Us (Email form and Social Media links), Newsletter sign up.
Nice to have
• Order Online
Should not have
• (Can't think of anything right now :-)

```html
<!DOCTYPE html>
<html lang="en">
<head>
<meta charset="utf-8">
<title>Bright Leaf Bistro &amp; Pantry</title>
<link href="https://fonts.googleapis.com/css2?family=Open+Sans:wght@400;600;700&family=Dancing+Script:wght@400;600&family=Cinzel:wght@600&display=swap" rel="stylesheet">
<style>
:root{
  --teal:#00a990;
  --orange:#f37122;
  --apricot:#faa54b;
  --aqua:#87cfc7;
  --cream:#f8f3ea;
  --ink:#333;
  --muted:#666;
  --footer:#2b2b2b;
  --footer-text:#bdbdbd;
}
*{box-sizing:border-box;margin:0;padding:0}
html,body{width:1200px;height:2612px;overflow:hidden}
body{background:var(--cream);font-family:"Open Sans",Arial,sans-serif;color:var(--ink);position:relative}
.abs{position:absolute}
.script{font-family:"Dancing Script",cursive;color:var(--teal);font-weight:400;text-align:center}
.section-title{font-family:"Open Sans",Arial,sans-serif;font-size:30px;font-weight:600;color:#444;text-align:center;letter-spacing:1px}
.section-title b{font-weight:700;color:#333}

/* header */
.site-header{top:0;left:0;width:1200px;height:179px;background:var(--cream)}
.brand{left:96px;top:66px;display:flex;align-items:center;gap:10px;font-size:21px;font-weight:700;color:var(--teal);white-space:nowrap}
.brand-dot{width:28px;height:28px;border-radius:50%;background:var(--apricot)}
.socials{left:540px;top:62px;display:flex;gap:8px}
.socials span{width:26px;height:26px;border-radius:50%;display:block}
.field-label{font-size:14px;font-weight:700;color:var(--teal);top:36px}
.field-label.news{color:var(--orange)}
.field{top:59px;height:32px;border:1px solid #ddd;background:#fff;font-size:11px;color:#999;padding:9px 14px;width:150px}
.field-btn{top:59px;width:31px;height:32px}
.vsep{top:38px;width:1px;height:56px;background:#ddd}
.main-nav{top:137px;left:0;width:1200px;height:20px;font-size:12px;color:#444}
.main-nav a{color:#444;text-decoration:none;position:absolute;top:0;white-space:nowrap}
.main-nav a.active{color:var(--teal)}

/* hero */
.hero{top:179px;left:0;width:1200px;height:419px;background:linear-gradient(180deg,#c46a2a 0%,#e89a3c 35%,#b9622a 55%,#8a4418 100%)}
.hero-caption{top:38px;width:100%;text-align:center;font-family:"Cinzel",serif;font-size:25px;color:#fff;letter-spacing:1px}
.hero-arrow{top:193px;width:24px;height:34px;background:rgba(0,0,0,.35)}

/* welcome */
.welcome-title{top:644px;width:100%;font-size:44px}
.welcome-text{top:716px;left:139px;width:922px;font-size:12.5px;line-height:21px;color:var(--muted);text-align:center}

/* marketplace */
.market{top:871px;left:0;width:1200px;height:369px;background:linear-gradient(90deg,#e9c67c,#f3dca2 40%,#f2d795 70%,#e8b870)}
.market .section-title{top:47px;width:100%}
.product{top:104px;width:235px;height:220px;background:#fff}
.product .photo{height:178px}
.product .label{height:42px;color:#fff;font-size:16px;font-weight:600;text-align:center;line-height:42px;letter-spacing:.5px}
.chev{top:190px}

/* events */
.events-title{top:1302px;width:100%;font-size:44px}
.event{top:1388px;width:470px;height:152px}
.event .photo{position:absolute;left:0;top:0;width:167px;height:152px}
.event .body{position:absolute;left:181px;top:0;width:289px}
.event h3{font-size:12.5px;font-weight:400;color:var(--orange);line-height:18px}
.event .date{font-size:13px;color:var(--teal);margin:12px 0 8px}
.event p{font-size:10.5px;line-height:16px;color:#555}
.event .more{font-size:10.5px;font-weight:600;color:#333;margin-top:6px}
.btn-view{top:1580px;left:554px;width:92px;height:33px;border:1px solid #ccc;background:#fff;font-size:11px;color:var(--orange);text-align:center;line-height:31px}

/* recipes */
.recipes{top:1693px;left:0;width:1200px;height:282px;background:linear-gradient(90deg,#e6d36a,#f2e59a 45%,#efe08a 70%,#e3c861)}
.recipes .section-title{top:34px;width:100%}
.recipe{top:91px;width:483px;height:146px;background:#fff}
.recipe .photo{position:absolute;left:0;top:0;width:166px;height:146px}
.recipe .body{position:absolute;left:184px;top:22px;width:280px}
.recipe h3{font-size:12.5px;font-weight:700;color:var(--orange);margin-bottom:10px}
.recipe p{font-size:10.5px;line-height:15px;color:#555}
.recipe .more{font-size:10.5px;font-weight:600;color:#333;margin-top:6px}

/* health */
.health-title{top:2032px;width:100%;font-size:44px}
.health-icon{top:2121px;left:206px;width:48px;height:48px}
.health-head{top:2113px;left:267px;font-size:17px;font-weight:400;color:var(--teal)}
.health-text{top:2144px;left:267px;width:714px;font-size:12px;line-height:19.5px;color:var(--muted)}

/* footer */
.site-footer{top:2303px;left:0;width:1200px;height:309px;background:var(--footer)}
.f-col{top:33px}
.f-col h4{font-size:13px;font-weight:400;color:#fff;margin-bottom:14px}
.f-col ul{list-style:none;font-size:11px;line-height:22.3px;color:var(--footer-text)}
.f-sep{top:40px;width:1px;height:150px;background:#444}
.f-rule{top:226px;left:99px;width:1002px;height:1px;background:#444}
.copyright{top:263px;left:99px;font-size:9.5px;color:#ccc}
.f-icons{top:257px;left:934px;display:flex;gap:8px}
.f-icons span{width:26px;height:26px;border-radius:50%;display:block}
</style>
</head>
<body>

<header class="site-header abs">
  <div class="brand abs"><span class="brand-dot"></span>Bright Leaf Bistro &amp; Pantry</div>
  <div class="socials abs" aria-label="Social media links">
    <span style="background:#2d5aa5"></span>
    <span style="background:#2aa6e0"></span>
    <span style="background:var(--orange)"></span>
    <span style="background:#4ea345;display:flex;align-items:center;justify-content:center">
      <svg width="14" height="10" viewBox="0 0 14 10"><rect x=".5" y=".5" width="13" height="9" fill="none" stroke="#fff"/><path d="M.5 .5 7 6 13.5 .5" fill="none" stroke="#fff"/></svg>
    </span>
  </div>
  <div class="field-label abs" style="left:704px">PRODUCT SEARCH</div>
  <div class="field abs" style="left:704px">Keyword</div>
  <div class="field-btn abs" style="left:854px;background:var(--aqua)">
    <svg width="31" height="32" viewBox="0 0 31 32"><circle cx="14" cy="14" r="5" fill="none" stroke="#fff" stroke-width="2"/><path d="M18 18l5 5" stroke="#fff" stroke-width="2"/></svg>
  </div>
  <div class="vsep abs" style="left:900px"></div>
  <div class="field-label news abs" style="left:918px">NEWSLETTER SUBSCRIBE</div>
  <div class="field abs" style="left:918px">E-mail ID</div>
  <div class="field-btn abs" style="left:1068px;background:var(--apricot)">
    <svg width="31" height="32" viewBox="0 0 31 32"><path d="M10 16h11M16 11l5 5-5 5" fill="none" stroke="#fff" stroke-width="2"/></svg>
  </div>
  <nav class="main-nav abs">
    <a class="active" style="left:479px">Home</a>
    <a style="left:540px">Events</a>
    <a style="left:603px">Cafe Menu</a>
    <a style="left:688px">Marketplace Products</a>
    <a style="left:829px">Health Info</a>
    <a style="left:916px">News</a>
    <a style="left:974px">Recipes</a>
    <a style="left:1042px">Contact Us</a>
  </nav>
</header>

<section class="hero abs" role="img" aria-label="Red and yellow apples on a wooden table with autumn leaves behind">
  <h1 class="hero-caption abs">PHASELLUS NISL EST, CONDIMENTUM VITAE FAUCIBUS IN.</h1>
  <div class="hero-arrow abs" style="left:0"></div>
  <div class="hero-arrow abs" style="right:0"></div>
</section>

<h2 class="welcome-title script abs">Welcome to Bright Leaf Bistro &amp; Pantry</h2>
<p class="welcome-text abs">Aenean sed quam non sapien faucibus consequat vitae sit amet orci. Praesent quis risus mi. In mollis nulla in pulvinar dictum. Vivamus interdum sagittis felis, ut dapibus ligula feugiat ac. In dictum sapien eu tellus finibus fermentum. Aenean faucibus lacus ut mollis commodo. Donec vestibulum odio sem, ac laoreet massa ullamcorper id. Donec molestie nisi et tellus hendrerit vehicula. Nunc eu ligula sed quam pulvinar maximus in vitae eros. Proin porta fermentum ipsum, vel porttitor turpis venenatis luctus. Vivamus volutpat eu sapien quis tempus. Aenean feugiat viverra lorem ac sagittis.</p>

<section class="market abs">
  <h2 class="section-title abs">MARKETPLACE <b>PRODUCTS</b></h2>
  <svg class="chev abs" style="left:26px" width="14" height="24" viewBox="0 0 14 24"><path d="M12 2 2 12l10 10" fill="none" stroke="#777" stroke-width="2"/></svg>
  <svg class="chev abs" style="left:1160px" width="14" height="24" viewBox="0 0 14 24"><path d="M2 2l10 10L2 22" fill="none" stroke="#777" stroke-width="2"/></svg>
  <div class="product abs" style="left:122px"><div class="photo" role="img" aria-label="Whole and halved orange" style="background:radial-gradient(circle,#f7a02a 0 32%,#fff 34%)"></div><div class="label" style="background:var(--orange)">ORANGE</div></div>
  <div class="product abs" style="left:361px"><div class="photo" role="img" aria-label="Bunch of green grapes" style="background:radial-gradient(circle,#a6c446 0 32%,#fff 34%)"></div><div class="label" style="background:var(--aqua)">GRAPE</div></div>
  <div class="product abs" style="left:601px"><div class="photo" role="img" aria-label="Mango with cubed half" style="background:radial-gradient(circle,#f2b530 0 32%,#fff 34%)"></div><div class="label" style="background:var(--apricot)">MANGO</div></div>
  <div class="product abs" style="left:841px"><div class="photo" role="img" aria-label="Whole and sliced limes" style="background:radial-gradient(circle,#7cbf3a 0 32%,#fff 34%)"></div><div class="label" style="background:var(--teal)">LIME</div></div>
</section>

<h2 class="events-title script abs">Latest Events &amp; Events</h2>
<article class="event abs" style="left:120px">
  <div class="photo" role="img" aria-label="Produce aisle stocked with fruit and vegetables" style="background:linear-gradient(135deg,#6a9a3a,#d7a33a,#b53a2a)"></div>
  <div class="body"><h3>Mauris suscipit felis id nunc elementum blan dit quam a ipsum gravida dapibus</h3><div class="date">APR 21, 2015</div><p>Fusce eget neque elit. Sed augue orci, elementum in magna congue, tincidunt vulputate erat. Aliquam consec tetur orci molestie dictum molestie. Proin eget congue nulla, vel tempor diam.</p><div class="more">MORE</div></div>
</article>
<article class="event abs" style="left:629px">
  <div class="photo" role="img" aria-label="Bread, cheese and milk on a table" style="background:linear-gradient(135deg,#4a3526,#9a7650,#e8dcc4)"></div>
  <div class="body"><h3>Mauris suscipit felis id nunc elementum blan dit quam a ipsum gravida dapibus</h3><div class="date">APR 21, 2015</div><p>Fusce eget neque elit. Sed augue orci, elementum in magna congue, tincidunt vulputate erat. Aliquam consec tetur orci molestie dictum molestie. Proin eget congue nulla, vel tempor diam.</p><div class="more">MORE</div></div>
</article>
<div class="btn-view abs">VIEW MORE</div>

<section class="recipes abs">
  <h2 class="section-title abs">LATEST <b>RECIPES</b></h2>
  <article class="recipe abs" style="left:99px">
    <div class="photo" role="img" aria-label="Chillies, carrots and spices with a wooden spoon" style="background:linear-gradient(135deg,#3a3a3a,#7a3a2a,#d9692a)"></div>
    <div class="body"><h3>PHASELLUS NISL CONDIMENTUM VITAE</h3><p>Fusce eget neque elit. Sed augue orci, elementum in magna congue, tincidunt vulputate erat. Aliquam consec tetur orci molestie dictum molestie.</p><div class="more">MORE</div></div>
  </article>
  <article class="recipe abs" style="left:617px">
    <div class="photo" role="img" aria-label="Chef plating a dish" style="background:linear-gradient(135deg,#1e1e1e,#4a3a30,#c9b8a8)"></div>
    <div class="body"><h3>PHASELLUS NISL CONDIMENTUM VITAE</h3><p>Fusce eget neque elit. Sed augue orci, elementum in magna congue, tincidunt vulputate erat. Aliquam consec tetur orci molestie dictum molestie.</p><div class="more">MORE</div></div>
  </article>
</section>

<h2 class="health-title script abs">Health Info</h2>
<svg class="health-icon abs" viewBox="0 0 48 48" aria-hidden="true"><circle cx="24" cy="24" r="24" fill="var(--teal)"/><circle cx="24" cy="13" r="3.5" fill="#fff"/><path d="M19 20h7v15h3v3H19v-3h3V23h-3z" fill="#fff"/></svg>
<h3 class="health-head abs">Aenean sed quam non sapien faucibus consequat vitae sit amet orci.</h3>
<p class="health-text abs">Aenean faucibus lacus ut mollis commodo. Donec vestibulum odio sem, ac laoreet massa ullamcorper id. Donec molestie nisi et tellus hendrerit vehicula. Nunc eu ligula sed quam pulvinar maximus in vitae eros. Proin porta fermentum ipsum, vel porttitor turpis venenatis luctus. Vivamus volutpat eu sapien quis tempus. Aenean feugiat viverra lorem ac sagittis. Donec sit amet lectus nec mi tempor laoreet ac nec nunc.</p>

<footer class="site-footer abs">
  <div class="f-col abs" style="left:101px"><h4>Quick Links</h4><ul><li>Home</li><li>Events</li><li>Cafe Menu</li><li>Marketplace</li><li>Products</li><li>Health Info</li></ul></div>
  <div class="f-col abs" style="left:232px"><h4>&nbsp;</h4><ul><li>News</li><li>Recipes</li><li>Contact Us</li><li>Search</li><li>Newsletter</li><li>Help</li></ul></div>
  <div class="f-sep abs" style="left:348px"></div>
  <div class="f-col abs" style="left:404px"><h4>Other Links</h4><ul><li>Pellentesque id</li><li>Suspendisse</li><li>Donec nec</li><li>Etiam et magna</li><li>Nunc porttitor</li><li>Phasellus</li></ul></div>
  <div class="f-sep abs" style="left:549px"></div>
  <div class="f-col abs" style="left:608px"><h4>Other Links</h4><ul><li>Pellentesque id</li><li>Suspendisse</li><li>Donec nec</li><li>Etiam et magna</li><li>Nunc porttitor</li><li>Phasellus</li></ul></div>
  <div class="f-sep abs" style="left:749px"></div>
  <div class="f-col abs" style="left:812px"><h4>Other Links</h4><ul><li>Pellentesque id</li><li>Suspendisse</li><li>Donec nec</li><li>Etiam et magna</li><li>Nunc porttitor</li><li>Phasellus</li></ul></div>
  <div class="f-sep abs" style="left:953px"></div>
  <div class="f-col abs" style="left:1016px"><h4>Other Links</h4><ul><li>Pellentesque id</li><li>Suspendisse</li><li>Donec nec</li><li>Etiam et magna</li><li>Nunc porttitor</li><li>Phasellus</li></ul></div>
  <div class="f-rule abs"></div>
  <p class="copyright abs">Copyright &copy; 2015 &nbsp;Bright Leaf Bistro &amp; Pantry. &nbsp;All rights reserved.</p>
  <div class="f-icons abs" aria-label="Social media links">
    <span style="background:#2d5aa5"></span>
    <span style="background:#2aa6e0"></span>
    <span style="background:var(--orange)"></span>
    <span style="background:#4ea345;display:flex;align-items:center;justify-content:center"><svg width="14" height="10" viewBox="0 0 14 10"><rect x=".5" y=".5" width="13" height="9" fill="none" stroke="#fff"/><path d="M.5 .5 7 6 13.5 .5" fill="none" stroke="#fff"/></svg></span>
    <span style="border:2px solid #888;display:flex;align-items:center;justify-content:center"><svg width="12" height="12" viewBox="0 0 12 12"><path d="M6 11V2M2 6l4-4 4 4" fill="none" stroke="#aaa" stroke-width="1.6"/></svg></span>
  </div>
</footer>

</body>
</html>
```